Business Card Design Project

This design is a slimline business card 45mm x90mm, the card will be printed at 49mm x 94mm and cut to 45mm x90 mm, this needs to be considered in the design. The content required on the front and back of the business card is attached in a pdf; the design will be done using photo shop as we use CS6 in our business. The design needs to be developed using a CMYK colour pallet, the main colours used on our business are red, grey black and white. A snapshot of our business brochure and new website has been provided to give you an understanding on our businesses look and feel.
FRONT OF BUSINESS CARD
Director
Marcus Fenwick
Ph+61 0421780213
www.brightlanepartners.com.au
marcusfenwick@brightlanepartners.com.au
BACK OF BUSINESS CARD
SUPPORTING CLIENTS IN
Oil & Gas I Minerals & Metals I Petrochemical I Manufacturing
Building & Construction I Telecommunication I Rail I Civil I New Industries
KNOWLEDGE I EXPERTISE I EXPERIENCE I CAPACITY

```html
<!DOCTYPE html>
<html lang="en">
<head>
<meta charset="utf-8">
<title>Marcus Fenwick — Business Card</title>
<link rel="stylesheet" href="https://fonts.googleapis.com/css2?family=EB+Garamond:wght@400;500&family=Stint+Ultra+Condensed&display=swap">
<style>
  :root {
    --page: #ffffff;
    --card-red: #b8161c;
    --card-red-deep: #9e0f14;
    --card-red-light: #c92a2c;
    --card-black: #1c1c1c;
    --card-black-light: #262626;
    --ink-white: #ffffff;
    --ink-grey: #b9b4b2;
  }
  * { margin: 0; padding: 0; box-sizing: border-box; }
  html, body {
    width: 1200px;
    height: 1200px;
    overflow: hidden;
    background: var(--page);
  }
  .canvas {
    position: relative;
    width: 1200px;
    height: 1200px;
    background: var(--page);
  }
  .card {
    position: absolute;
    left: 126px;
    width: 956px;
    height: 442px;
    overflow: hidden;
  }
  .red-weave {
    background-color: var(--card-red);
    background-image:
      repeating-linear-gradient(0deg, rgba(0,0,0,0.10) 0 1px, transparent 1px 4px),
      repeating-linear-gradient(90deg, rgba(255,255,255,0.05) 0 2px, transparent 2px 5px),
      radial-gradient(ellipse at 30% 40%, var(--card-red-light), var(--card-red-deep));
  }
  .card--front { top: 48px; }
  .card--back {
    top: 634px;
    background-color: var(--card-black);
    background-image:
      repeating-linear-gradient(45deg, rgba(255,255,255,0.025) 0 1px, transparent 1px 3px),
      radial-gradient(ellipse at 40% 40%, var(--card-black-light), var(--card-black));
  }
  .name {
    position: absolute;
    left: 354px;
    top: 66px;
    font-family: "EB Garamond", serif;
    font-weight: 400;
    font-size: 80px;
    line-height: 1;
    color: var(--ink-white);
    white-space: nowrap;
  }
  .role {
    position: absolute;
    left: 378px;
    top: 160px;
    font-family: "EB Garamond", serif;
    font-size: 27px;
    line-height: 1;
    color: var(--ink-grey);
    letter-spacing: 0.5px;
  }
  .contact {
    position: absolute;
    left: 97px;
    top: 282px;
    font-family: "EB Garamond", serif;
    font-size: 23px;
    line-height: 27.5px;
    color: var(--ink-white);
    letter-spacing: 0.4px;
    list-style: none;
    white-space: nowrap;
  }
  .sectors {
    position: absolute;
    left: 0;
    top: 0;
    width: 956px;
    height: 382px;
  }
  .sectors text {
    font-family: "Stint Ultra Condensed", serif;
    fill: var(--ink-white);
  }
  .sectors .heading { font-size: 33px; }
  .sectors .list { font-size: 34px; }
  .band {
    position: absolute;
    left: 0;
    bottom: 0;
    width: 100%;
    height: 60px;
  }
</style>
</head>
<body>
<main class="canvas">
  <section class="card card--front red-weave" aria-label="Card front">
    <h1 class="name">Marcus Fenwick</h1>
    <p class="role">Director</p>
    <ul class="contact">
      <li>Ph+61 0437925846</li>
      <li>www.brightlanepartners.com.au</li>
      <li>marcusfenwick@brightlanepartners.com.au</li>
    </ul>
  </section>

  <section class="card card--back" aria-label="Card back">
    <svg class="sectors" viewBox="0 0 956 382" xmlns="http://www.w3.org/2000/svg">
      <text class="heading" x="80" y="117" textLength="271" lengthAdjust="spacingAndGlyphs">SUPPORTING CLIENTS IN</text>
      <text class="list" x="80" y="170" textLength="654" lengthAdjust="spacingAndGlyphs">Oil &amp; Gas I Minerals &amp; Metals I Petrochemical I Manufacturing</text>
      <text class="list" x="80" y="218" textLength="792" lengthAdjust="spacingAndGlyphs">Building &amp; Construction I Telecommunication I Rail I Civil I New Industries</text>
    </svg>
    <div class="band red-weave"></div>
  </section>
</main>
</body>
</html>
```